Book & e-book cover - front, back and sleeve

Please see plot description:

The Lantern

A man lies dying and trapped in a parking garage stairwell. The poorly lit stairwell serves as a painful reminder of one of his memories of childhood locked in that darkened closet. To keep himself in tact he would play with a shiny silver button he ripped off from his pajamas – throwing it in the air and tapping the floor to find it. As he lies trapped and dying that same defeated and abandoned feeling descends upon him. As he comes in and out of consciousness memories from his past manifest themselves and we are introduced to the turbulent and sometimes triumphant pathway that has led him to his current state. It is up to him to sort through the barrage of emotions to find his way out, to let go, to forgive. That is if his heart will let him.
Updates

I know that we mentioned having a photograph of a button on the cover but we would like to see examples of covers with a more abstract or drawn or painted looking button.  Thanks.

Target Market(s)

Dramatic story - geared towards adult readers

Industry/Entity Type

Parking

Requirements
Must have
• Simple, crisp, custom, classic look. Do not want it to look to sci-fi or medival - this is an emotional story - a memoir.

Items on the front cover:

Title: The Lantern
Author: R.M. Halvorsen
Words: A Novel
Photo: a sliver button (just one image)

Items on the back cover

Plot description area
ISBN area at bottom

Nice to have
• Please see examples that have been uploaded. I like novels with a textured background.

A simple button on the cover with the right fonts and colour scheme.
Should not have
• I do not want a person or icons used on the cover
I do not want it to busy.
Do not want it to feel like it is a sci-fi novel or medival story.
Do not want the cover to be too "dark" - I do not want potential readers to get the wrong idea of what "The Lantern" is about.

```html
<!DOCTYPE html>
<html lang="en">
<head>
<meta charset="utf-8">
<title>The Lantern — R.M. Halvorsen</title>
<link rel="stylesheet" href="https://fonts.googleapis.com/css2?family=Tenor+Sans&display=swap">
<style>
  :root {
    --page: #ffffff;
    --cover-rose: #c0787b;
    --cover-rose-light: #cd8a8c;
    --cover-rose-deep: #b06a6e;
    --cover-edge: #9a8a8a;
    --ink-light: #ffffff;
    --silver-hi: #eef0ee;
    --silver-mid: #b9bebd;
    --silver-low: #7f8786;
  }
  * { margin: 0; padding: 0; box-sizing: border-box; }
  html, body {
    width: 1200px;
    height: 1000px;
    overflow: hidden;
    background: var(--page);
  }
  .stage {
    position: relative;
    width: 1200px;
    height: 1000px;
  }
  .cover {
    position: absolute;
    left: 318px;
    top: 42px;
    width: 570px;
    height: 913px;
    border: 1px solid var(--cover-edge);
    background:
      radial-gradient(ellipse at 30% 20%, var(--cover-rose-light) 0%, transparent 60%),
      radial-gradient(ellipse at 80% 85%, var(--cover-rose-deep) 0%, transparent 55%),
      var(--cover-rose);
    font-family: "Tenor Sans", sans-serif;
    color: var(--ink-light);
    text-align: center;
  }
  .title {
    position: absolute;
    left: 0;
    right: 0;
    top: 56px;
    font-weight: 400;
    line-height: 1;
  }
  .title-article {
    display: block;
    font-size: 66px;
    letter-spacing: 1px;
  }
  .title-main {
    display: block;
    margin-top: 26px;
    font-size: 80px;
    letter-spacing: 1px;
  }
  .button-art {
    position: absolute;
    left: 103px;
    top: 260px;
    width: 366px;
    height: 366px;
    border-radius: 50%;
    background: radial-gradient(circle at 40% 35%, var(--silver-hi) 0%, var(--silver-mid) 55%, var(--silver-low) 100%);
    box-shadow: 6px 10px 18px rgba(80, 30, 35, 0.35);
  }
  .author {
    position: absolute;
    left: 0;
    right: 0;
    top: 742px;
    font-size: 58px;
    line-height: 1;
    text-transform: lowercase;
  }
  .rule {
    position: absolute;
    left: 92px;
    top: 807px;
    width: 372px;
    height: 2px;
    background: var(--ink-light);
  }
  .format {
    position: absolute;
    left: 0;
    right: 0;
    top: 829px;
    font-size: 21px;
    letter-spacing: 1px;
  }
</style>
</head>
<body>
  <div class="stage">
    <div class="cover">
      <h1 class="title">
        <span class="title-article">THE</span>
        <span class="title-main">LANTERN</span>
      </h1>
      <div class="button-art" role="img" aria-label="A single shiny silver four-hole button"></div>
      <p class="author">r. m. halvorsen</p>
      <div class="rule"></div>
      <p class="format">A NOVEL</p>
    </div>
  </div>
</body>
</html>
```